Vel Moro A4 paper and card metallic new packaging

Vel Moro New Packaging Brief
We need a CLASSIC packaging design which wraps around the bottom left side of the product (A4 card) in the shape of a square (front & back) for an existing brand name call Vel Moro. This is then covered in a polybag. This needs to display the most important detail about the product on the FRONT and then the other information on the back.
See images attached of some ideas
The packaging needs to be CLEAN and simple to portray the fact the product is of a Premium Luxurious quality.
It is sold in a store where it sits on a shelf so we need the following information portrayed very clearly so the consumer can see it straight away and know what the product is:
The below points need to be shown on the FRONT of the packaging - Information is listed in order of importance.
1.Premium Luxurious Card
2. Metallic
3. A4
4.The Colour (eg, Silver)
5.25 Pack
6. Logo – this can be small

These need to be shown on the BACK of the packaging - Information is listed in order of importance.
1.PREMIUM Luxurious Card
2.
• Ideal for card making for all occasions
• Invitations for all Celebrations
• Creative card & paper for presentations
3. Acid free
4. Made in china
5. Logo – this can be small
6.Barcode

Background
Vel Moro is a brand which sells PREMIUM Luxurious Paper and card stock which can be used for card making, invites, presentations. The colour range is approx. 24 colours and it comes in metallic and weave. It includes the following
*A4 Card 260gsm & paper 120gsm
*DL & C6 envelopes 120gsm

PLEASE READ ALL UPLOADED FILE NAMES.

Target Market(s)

Office supply and invitation market

Industry/Entity Type

Store

Requirements
Must have
• Most important is to have a style of packaging that suits and displays the product. Needs to be fresh and clean packaging but also show quality and show the actual product.
• Font should be simple, easy to read, clear so consumers can read what the product is straight away.
• Colours – can match the logo but we are open to other ideas as well.
• The colour range of the card we sell is 24 different colours so the actual packaging needs to match all colours and stand out.

```html
<!DOCTYPE html>
<html lang="en">
<head>
<meta charset="utf-8">
<title>Vel Moro Premium Luxurious Card Packaging</title>
<link rel="stylesheet" href="https://fonts.googleapis.com/css2?family=Source+Sans+3:wght@400;600&family=Crimson+Pro:wght@400&display=swap">
<style>
  :root {
    --backdrop: #e9a9c4;
    --header: #1b1b1b;
    --sleeve: #ffffff;
    --accent: #a84e8a;
    --brand: #3fb8c4;
    --ink-light: #ffffff;
  }
  * { box-sizing: border-box; margin: 0; padding: 0; }
  html, body { width: 1200px; height: 1060px; overflow: hidden; }
  body { background: var(--backdrop); position: relative; font-family: "Source Sans 3", sans-serif; }

  .package {
    position: absolute;
    background: var(--sleeve);
    box-shadow: 8px 14px 22px rgba(60, 20, 40, 0.35);
    overflow: hidden;
  }
  .package--front { left: 123px; top: 123px; width: 469px; height: 797px; }
  .package--back  { left: 619px; top: 206px; width: 467px; height: 793px; }

  .header {
    position: relative;
    height: 130px;
    background: var(--header);
    color: var(--ink-light);
  }
  .brand-name {
    position: absolute;
    left: 26px; top: 36px;
    font-family: "Source Sans 3", sans-serif;
    font-weight: 400;
    font-size: 30px;
    color: var(--brand);
    letter-spacing: 0.5px;
  }
  .product-title {
    position: absolute;
    left: 22px; top: 96px;
    font-size: 18px;
    font-weight: 400;
  }
  .hang-hole { position: absolute; left: 204px; top: 26px; }
  .feature-list {
    position: absolute;
    left: 304px; top: 44px;
    font-family: "Crimson Pro", serif;
    font-size: 16px;
    line-height: 16px;
    list-style: disc;
    padding-left: 18px;
  }

  .swatch-strip { display: flex; height: 17px; }
  .swatch-strip span { flex: 1; }

  .floral-band { position: absolute; left: 0; top: 147px; }

  .info-panel {
    position: absolute;
    left: 0; bottom: 0;
    width: 100%; height: 141px;
    background: var(--accent);
    color: var(--ink-light);
  }
  .info-list {
    position: absolute;
    left: 36px; top: 20px;
    font-family: "Crimson Pro", serif;
    font-size: 13.5px;
    line-height: 15.5px;
    list-style: none;
  }
  .info-list li::before { content: "• "; }
  .info-list .continued { padding-left: 8px; }
  .info-list .continued::before { content: ""; }
</style>
</head>
<body>

<section class="package package--front">
  <header class="header">
    <span class="brand-name">Vel Moro</span>
    <svg class="hang-hole" width="62" height="16" viewBox="0 0 62 16" aria-hidden="true">
      <path d="M6 5 H24 Q31 -3 38 5 H56 A5.5 5.5 0 0 1 56 16 H6 A5.5 5.5 0 0 1 6 5 Z" fill="#fff"/>
    </svg>
    <h1 class="product-title">Premium Luxurious Card</h1>
    <ul class="feature-list">
      <li>Metallic</li>
      <li>A4</li>
      <li>The Colour (Pink)</li>
      <li>25Pack</li>
    </ul>
  </header>
  <div class="swatch-strip">
    <span style="background:#2e3f8a"></span><span style="background:#d4d84a"></span><span style="background:#a8422e"></span><span style="background:#c97b35"></span><span style="background:#1f4e4a"></span><span style="background:#8a2230"></span><span style="background:#8c6fa6"></span><span style="background:#d63048"></span><span style="background:#e86b30"></span><span style="background:#f5edc0"></span><span style="background:#3b3626"></span><span style="background:#8a8662"></span><span style="background:#7e4a8c"></span><span style="background:#13a38a"></span><span style="background:#1c2a52"></span><span style="background:#e07fa8"></span><span style="background:#b02a4a"></span><span style="background:#5b2d73"></span><span style="background:#fff59a"></span><span style="background:#1c2420"></span><span style="background:#9bbbd8"></span><span style="background:#d92c3a"></span><span style="background:#136b3a"></span><span style="background:#d62060"></span><span style="background:#12a8dc"></span><span style="background:#4a0a2a"></span><span style="background:#4caf5a"></span><span style="background:#0a7aa8"></span><span style="background:#6e2a55"></span><span style="background:#d41e7a"></span>
  </div>
  <svg class="floral-band" width="469" height="650" viewBox="0 0 469 650" role="img" aria-label="Cascading white-outlined flower pattern on magenta, framing the lower left corner">
    <path d="M0 0 H85 Q68 40 60 75 L60 240 Q78 340 120 400 Q215 470 320 545 Q400 560 469 575 V650 H0 Z" fill="var(--accent)"/>
  </svg>
</section>

<section class="package package--back">
  <header class="header">
    <span class="brand-name">Vel Moro</span>
    <svg class="hang-hole" width="62" height="16" viewBox="0 0 62 16" aria-hidden="true">
      <path d="M6 5 H24 Q31 -3 38 5 H56 A5.5 5.5 0 0 1 56 16 H6 A5.5 5.5 0 0 1 6 5 Z" fill="#fff"/>
    </svg>
    <h1 class="product-title">Premium Luxurious Card</h1>
    <ul class="feature-list">
      <li>Metallic</li>
      <li>A4</li>
      <li>The Colour (Blue)</li>
      <li>25Pack</li>
    </ul>
  </header>
  <div class="swatch-strip">
    <span style="background:#2e3f8a"></span><span style="background:#d4d84a"></span><span style="background:#a8422e"></span><span style="background:#c97b35"></span><span style="background:#1f4e4a"></span><span style="background:#8a2230"></span><span style="background:#8c6fa6"></span><span style="background:#d63048"></span><span style="background:#e86b30"></span><span style="background:#f5edc0"></span><span style="background:#3b3626"></span><span style="background:#8a8662"></span><span style="background:#7e4a8c"></span><span style="background:#13a38a"></span><span style="background:#1c2a52"></span><span style="background:#e07fa8"></span><span style="background:#b02a4a"></span><span style="background:#5b2d73"></span><span style="background:#fff59a"></span><span style="background:#1c2420"></span><span style="background:#9bbbd8"></span><span style="background:#d92c3a"></span><span style="background:#136b3a"></span><span style="background:#d62060"></span><span style="background:#12a8dc"></span><span style="background:#4a0a2a"></span><span style="background:#4caf5a"></span><span style="background:#0a7aa8"></span><span style="background:#6e2a55"></span><span style="background:#d41e7a"></span>
  </div>
  <div class="info-panel">
    <ul class="info-list">
      <li>PREMIUM Luxurious Card</li>
      <li>Ideal for card making for all occasions</li>
      <li>Invitations for all Celebrations</li>
      <li class="continued">Creative card &amp; paper for presentations</li>
      <li>Acid free</li>
      <li>Made in china</li>
    </ul>
  </div>
</section>

</body>
</html>
```